Business card design for online Mandarin Learning School

We need a business card design for our online language learning school called "Maple Bridge Online for Mandarin Learning". Our existing website is https://www.maplebridgeonline.com
We have our logo already. We would like to see our business card design that can make our online teaching services to be innovative, young, energetic and fun to learn. Prefer to have a certain level of color matching with our website. Apart from "Maple Bridge Online", need to specifically state "for Mandarin Learning" as well on the business card.

```html
<!DOCTYPE html>
<html lang="en">
<head>
<meta charset="utf-8">
<title>Maple Bridge Online for Mandarin Learning — Business Card</title>
<link rel="stylesheet" href="https://fonts.googleapis.com/css2?family=Cinzel:wght@400&family=Arimo:wght@400&display=swap">
<style>
  :root {
    --teal: #22a9b3;
    --coral: #e05a5c;
    --slate: #767676;
    --slate-dark: #666666;
    --paper: #ffffff;
    --cream: #f1f1e6;
    --backdrop: #e8ecec;
    --serif: "Cinzel", "Times New Roman", serif;
    --sans: "Arimo", Arial, sans-serif;
  }
  * { box-sizing: border-box; margin: 0; padding: 0; }
  html, body { width: 1200px; height: 900px; overflow: hidden; }
  body {
    background: var(--backdrop);
    display: flex;
    flex-direction: column;
    align-items: center;
    justify-content: center;
    gap: 40px;
  }
  .card {
    position: relative;
    width: 700px;
    height: 400px;
    background: var(--paper);
    box-shadow: 0 6px 18px rgba(0,0,0,0.12);
    overflow: hidden;
  }
  .stripe {
    position: absolute;
    left: 14px;
    right: 14px;
    height: 5px;
    display: flex;
  }
  .stripe span { display: block; height: 100%; }
  .stripe--top { top: 14px; }
  .stripe--bottom { bottom: 14px; }
  .stripe .teal { background: var(--teal); }
  .stripe .coral { background: var(--coral); }
  .stripe .slate { background: var(--slate); }

  /* Front */
  .brand {
    position: absolute;
    inset: 0;
    display: flex;
    align-items: center;
    justify-content: center;
    gap: 18px;
  }
  .brand__dot {
    width: 22px;
    height: 22px;
    border-radius: 50%;
    background: var(--coral);
  }
  .brand__name {
    font-family: var(--serif);
    font-weight: 400;
    font-size: 54px;
    letter-spacing: 3px;
    color: var(--teal);
  }

  /* Back */
  .wordmark {
    position: absolute;
    left: 190px;
    top: 40px;
    width: 460px;
    height: 118px;
    background: var(--cream);
    padding: 14px 22px 0;
  }
  .wordmark__name {
    font-family: var(--serif);
    font-size: 44px;
    letter-spacing: 2px;
    color: var(--teal);
    line-height: 1;
    white-space: nowrap;
  }
  .wordmark__rule {
    height: 4px;
    margin: 8px 0 6px;
    background: var(--slate);
  }
  .wordmark__url {
    font-family: var(--serif);
    font-size: 19px;
    letter-spacing: 1px;
    color: var(--coral);
    white-space: nowrap;
  }
  .tagline {
    position: absolute;
    left: 300px;
    top: 178px;
    font-family: var(--sans);
    font-size: 20px;
    color: var(--coral);
  }
  .contacts {
    position: absolute;
    left: 190px;
    right: 12px;
    bottom: 12px;
    height: 170px;
    display: flex;
  }
  .tile {
    flex: 1;
    display: flex;
    flex-direction: column;
    align-items: center;
    justify-content: center;
    gap: 14px;
    color: var(--paper);
    font-family: var(--sans);
    font-size: 15px;
    text-align: center;
    line-height: 1.2;
  }
  .tile--name { background: var(--teal); }
  .tile--email { background: var(--coral); }
  .tile--phone { background: var(--slate-dark); }
  .tile svg { width: 54px; height: 54px; fill: var(--paper); }
</style>
</head>
<body>

  <section class="card card--front" aria-label="Business card front">
    <div class="stripe stripe--top">
      <span class="teal" style="width:30%"></span><span class="coral" style="width:32%"></span><span class="slate" style="width:38%"></span>
    </div>
    <div class="brand">
      <span class="brand__dot"></span>
      <span class="brand__name">MAPLE BRIDGE</span>
    </div>
    <div class="stripe stripe--bottom">
      <span class="teal" style="width:30%"></span><span class="coral" style="width:32%"></span><span class="slate" style="width:38%"></span>
    </div>
  </section>

  <section class="card card--back" aria-label="Business card back">
    <div class="stripe stripe--top">
      <span class="teal" style="width:32%"></span><span class="coral" style="width:30%"></span><span class="slate" style="width:38%"></span>
    </div>

    <div class="wordmark">
      <div class="wordmark__name">MAPLE BRIDGE</div>
      <div class="wordmark__rule"></div>
      <div class="wordmark__url">WWW.MAPLEBRIDGEONLINE.COM</div>
    </div>

    <p class="tagline">for Mandarin Learning</p>

    <div class="contacts">
      <div class="tile tile--name">
        <svg viewBox="0 0 54 54" aria-hidden="true">
          <circle cx="27" cy="16" r="12"/>
          <path d="M6 50 C6 36 14 30 27 30 C40 30 48 36 48 50 Z"/>
        </svg>
        <span>Your Name</span>
      </div>
      <div class="tile tile--email">
        <svg viewBox="0 0 54 54" aria-hidden="true">
          <path d="M4 12 H50 V42 H4 Z M8 15 L27 30 L46 15 Z" fill-rule="evenodd"/>
        </svg>
        <span>hello@maplebridgeonline.com</span>
      </div>
      <div class="tile tile--phone">
        <svg viewBox="0 0 54 54" aria-hidden="true">
          <path d="M16 6 L24 6 L26 16 L20 19 C22 27 26 32 33 35 L36 29 L46 31 L46 39 C46 44 42 48 36 47 C20 44 10 32 8 16 C7 10 11 6 16 6 Z"/>
        </svg>
        <span>000.000.0000<br>000.000.0000</span>
      </div>
    </div>
  </section>

</body>
</html>
```